Photography Prints Business Card Design

Background info: Nature, flower, landscape,  macro, wildlife photographer. Shoot color and B&W images. Sell prints at juried fine art shows.
Looking for two-sided, clean, memorable design with creative use of my initials, DK.   I like the DK symbol in the my logo. Just use the DK symbol. Do not leave the underlying text as uploaded by me. I do not like the serif font and positioning of the words!  Either  remove the small print "Dorian Kessler Photography" under the logo,  or change to a sans serif font, or reposition with "Dorian Kessler" above "Photography" which seems to work with serif fonts.
Target Market(s)
Sophisticated art buyers, post-college to middle age
Industry/Entity Type
Business
Contact Information for Business Card
Dorian Kessler Photography
842 Harrow Bend CT
Winston-Salem, NC 27127
(828) 555-0148
www.doriankessler.com
PW:kesslerphoto
dorian@doriankessler.com
If using just one line address, make sure there is a comma after  "CT" in street address. For example:
842 Harrow Bend CT, Winston-Salem, NC 27127
Requirements
Must have
- 1.Two-sided card submitted as one design.
2. Must use the DK symbol in my logo.
3. Do not leave the text "Dorian Kessler Photography" under the DK symbol in the logo uploaded by me. I do not like that serif font or the positioning of the words! Either remove the small print "Dorian Kessler Photography" under the logo entirely, or change text to a sans serif font, or reposition text with "Dorian Kessler" above "Photography" which seems to work with serif fonts.
Nice to have
- Can use my DK logo (three file types uploaded: AI, PSD, TIF)  I  like the attached B&W water droplet photo.  My pictures on my website, www.doriankkessler.com  can also be used.  Possible use of Pinwave logo with (either the "f" alone or the square blue icon with white "f") my PW page short url name: kesslerphoto.
Should not have
- 1.No icons or pictures  of camera or lenses or other photographic gear or film strips.
2. No QR or other "barcode" type symbols.
3. No outlining of my logo symbol (drop shadow possibly).
4. No decorative or outlined fonts.
5. I am not a fan of most script fonts.
6. No play on "Kessler" such as snow or other winter season symbols.
7. Do not keep the original text, "Dorian Kessler Photography" under DK logo. Change it or remove it entirely.

```html
<!DOCTYPE html>
<html lang="en">
<head>
<meta charset="utf-8">
<title>Dorian Kessler Photography – Business Card</title>
<link rel="stylesheet" href="https://fonts.googleapis.com/css2?family=Roboto:wght@300&family=Roboto+Condensed:wght@300&display=swap">
<style>
  :root {
    --stage-light: #f4f4f4;
    --stage-dark: #c4c5c7;
    --card: #58585a;
    --card-mark: #6c6d70;
    --logo-grey: #a2a3a5;
    --contact-text: #f0f0f0;
  }
  * { margin: 0; padding: 0; box-sizing: border-box; }
  html, body { width: 1200px; height: 900px; overflow: hidden; }
  body {
    position: relative;
    background: radial-gradient(ellipse at center, var(--stage-light) 35%, var(--stage-dark) 100%);
    font-family: "Roboto", sans-serif;
  }
  .card {
    position: absolute;
    left: 233px;
    width: 730px;
    height: 414px;
    border-radius: 22px;
    background: var(--card);
    overflow: hidden;
  }
  .card--front { top: 17px; }
  .card--back { top: 461px; }

  .brand__initials {
    position: absolute; left: 188px; top: 150px;
    font-family: "Roboto", sans-serif; font-weight: 300;
    font-size: 76px; line-height: 1; color: var(--logo-grey);
    letter-spacing: -2px;
  }
  .brand__name {
    position: absolute; left: 309px; top: 168px;
    font-family: "Roboto", sans-serif; font-weight: 300;
    font-size: 37px; line-height: 1; color: var(--logo-grey);
    letter-spacing: -0.5px; white-space: nowrap;
  }
  .brand__tagline {
    position: absolute; left: 311px; top: 210px;
    font-family: "Roboto", sans-serif; font-weight: 300;
    font-size: 14px; line-height: 1; color: var(--logo-grey);
    letter-spacing: 7.2px; white-space: nowrap;
  }

  .back-initials {
    position: absolute; left: 200px; top: -80px;
    font-family: "Roboto", sans-serif; font-weight: 300;
    font-size: 560px; line-height: 1; color: var(--card-mark);
    letter-spacing: -20px; white-space: nowrap;
  }
  .contact {
    position: absolute; left: 51px; top: 0;
    font-style: normal;
    font-family: "Roboto Condensed", sans-serif; font-weight: 300;
    color: var(--contact-text); font-size: 18.5px; line-height: 1;
  }
  .contact__line { position: absolute; left: 0; white-space: nowrap; display: flex; align-items: center; }
  .contact__line--address1 { top: 128px; }
  .contact__line--address2 { top: 160px; }
  .contact__line--phone { top: 222px; font-size: 19.5px; }
  .contact__line--web { top: 287px; }
  .contact__line--social { top: 319px; }
  .contact__line--email { top: 351px; }
  .contact__square {
    display: inline-block; width: 16px; height: 16px;
    background: var(--contact-text); margin-right: 6px;
  }
</style>
</head>
<body>
  <section class="card card--front" aria-label="Card front">
    <span class="brand__initials">DK</span>
    <span class="brand__name">Dorian Kessler</span>
    <span class="brand__tagline">PHOTOGRAPHY</span>
  </section>

  <section class="card card--back" aria-label="Card back">
    <span class="back-initials" aria-hidden="true">DK</span>
    <address class="contact">
      <span class="contact__line contact__line--address1">842 Harrow Bend CT</span>
      <span class="contact__line contact__line--address2">Marlow-Heights NC 28419</span>
      <span class="contact__line contact__line--phone">(828) 555-0148</span>
      <span class="contact__line contact__line--web">www.doriankessler.com</span>
      <span class="contact__line contact__line--social"><span class="contact__square"></span>kesslerphoto</span>
      <span class="contact__line contact__line--email">dorian@doriankessler.com</span>
    </address>
  </section>
</body>
</html>
```